Portrait of a Learner Infographic

A portrait of a learner is an aspirational idea of the skills a student should have at graduation. "Learner" recognizes that learning continues after graduation.
An info graphic is needed to convey the skills that have been identified. A full version is needed that can be posted on classroom walls (11x17) and a simplified version to share on the website and any other means identified.
The Brambleton School District is in Concord, New Hampshire, the capital city for NH. The district serves 4,100 diverse students in seven schools and a regional career and technical education center.
The district's hex colors are Green: #007137 and Blue: #085bab
Each school has its own unique colors.
The design should be positive, aspirational and still professional.
Teachers, students and parents
Public school district

```html
<!DOCTYPE html>
<html lang="en">
<head>
<meta charset="utf-8">
<title>Portrait of a Learner – Brambleton School District</title>
<link href="https://fonts.googleapis.com/css2?family=Exo+2:wght@300;400;700;800&family=Libre+Baskerville&display=swap" rel="stylesheet">
<style>
  :root{
    --page:#eef5e6;
    --paper:#ffffff;
    --brand-green:#0f8a44;
    --green-a:#45b649;
    --green-b:#6dbd44;
    --band-green:#0aa64b;
    --navy:#0b2d55;
    --blue:#00446f;
    --cell-light:#eeeeef;
    --cell-dark:#dedfe1;
    --text-body:#3d3d3d;
    --text-muted:#555;
    --swoosh-1:#c2c1c6;
    --swoosh-2:#d9dbd9;
    --swoosh-3:#ececec;
  }
  *{box-sizing:border-box;margin:0;padding:0}
  html,body{width:1200px;height:1200px;overflow:hidden;background:var(--page)}
  body{display:flex;justify-content:center;align-items:center;font-family:"Exo 2",sans-serif}
  .poster{position:relative;width:780px;height:1200px;background:var(--paper);overflow:hidden;border:1px solid #9a9a9a}
  .swooshes{position:absolute;inset:0}
  .district-name{position:absolute;left:62px;top:52px;font-family:"Libre Baskerville",serif;font-size:17px;color:var(--brand-green);line-height:1.25}
  .title{position:absolute;left:58px;top:138px;font-weight:800;font-size:40px;color:var(--brand-green);letter-spacing:.5px}
  .intro{position:absolute;left:58px;top:188px;width:540px;font-weight:300;font-size:11.6px;color:var(--text-muted);line-height:1.3}
  .pillar{position:absolute;left:58px;width:665px;height:272px;
    background:linear-gradient(90deg,var(--green-a) 0,var(--green-b) 350px,var(--navy) 350px,var(--navy) 494px,var(--blue) 494px)}
  .pillar .pointer{position:absolute;left:328px;top:272px}
  .pillar-art{position:absolute;left:22px;top:56px;width:166px;height:145px;border-radius:6px;
    background:linear-gradient(160deg,#5cc058,#c7cde6 70%,#9fa3b2)}
  .pillar-label{position:absolute;left:0;top:201px;width:204px;height:45px;background:var(--band-green);
    color:#fff;font-weight:800;font-size:17px;display:flex;align-items:center;justify-content:center;letter-spacing:.3px}
  .traits{position:absolute;left:204px;top:21px;width:436px;height:225px;background:#fff;padding:3px;
    display:grid;grid-template-columns:repeat(3,1fr);grid-template-rows:1fr 1fr;gap:3px}
  .trait{padding:14px 10px 0 10px}
  .trait:nth-child(odd){background:var(--cell-light)}
  .trait:nth-child(even){background:var(--cell-dark)}
  .trait-head{display:flex;align-items:center;gap:6px;height:26px;margin-bottom:10px}
  .trait-num{flex:none;width:23px;height:23px;border-radius:50%;background:var(--band-green);color:#fff;
    font-weight:800;font-size:11px;display:flex;align-items:center;justify-content:center}
  .trait-name{color:var(--band-green);font-weight:800;font-size:9.6px;line-height:1.2;text-transform:uppercase}
  .trait-text{font-size:7.3px;color:var(--text-body);line-height:1.3}
  .trait.locked{display:flex;align-items:center;justify-content:center;padding:0}
</style>
</head>
<body>
<div class="poster">
  <svg class="swooshes" width="780" height="1200" viewBox="0 0 780 1200" aria-hidden="true">
    <path d="M540 0 L780 0 L780 245 C720 150 650 60 540 0Z" fill="var(--swoosh-1)"/>
    <path d="M400 0 L540 0 C650 60 720 150 780 245 L780 440 C700 240 580 70 400 0Z" fill="var(--swoosh-3)"/>
    <path d="M470 0 C600 60 700 180 770 420 C690 210 590 80 470 0Z" fill="var(--swoosh-2)"/>
    <path d="M0 540 C80 740 220 1000 460 1200 L0 1200Z" fill="var(--swoosh-1)"/>
    <path d="M0 580 C120 860 320 1080 600 1200 L460 1200 C220 1000 80 740 0 560Z" fill="var(--swoosh-3)"/>
    <path d="M0 650 C140 900 330 1080 580 1170 L780 1190 L780 1200 L560 1200 C300 1080 110 880 0 680Z" fill="var(--swoosh-2)"/>
  </svg>

  <div class="district-name">BRAMBLETON<br>School District</div>
  <h1 class="title">PORTRAIT OF A LEARNER</h1>
  <p class="intro">Brambleton School District learners are informed, compassionate and capable citizens who effectively, courageously and responsibly direct their lives and positively impact communities</p>

  <section class="pillar" style="top:239px">
    <div class="pillar-art" role="img" aria-label="Illustration of a student with a light bulb idea"></div>
    <div class="pillar-label">SKILLFUL</div>
    <div class="traits">
      <div class="trait"><div class="trait-head"><span class="trait-num">01</span><span class="trait-name">Analytical<br>Thinker</span></div><p class="trait-text">Respectfully engages with others, Asks challenging and probing questions in a manner that preserves healthy relationships</p></div>
      <div class="trait"><div class="trait-head"><span class="trait-num">02</span><span class="trait-name">Informed<br>Risk-Taker</span></div><p class="trait-text">Respectfully engages with others, Asks challenging and probing questions in a manner that preserves healthy relationships</p></div>
      <div class="trait"><div class="trait-head"><span class="trait-num">03</span><span class="trait-name">Self-<br>Motivated</span></div><p class="trait-text">Respectfully engages with others, Asks challenging and probing questions in a manner that preserves healthy relationships</p></div>
      <div class="trait"><div class="trait-head"><span class="trait-num">04</span><span class="trait-name">Innovative</span></div><p class="trait-text">Respectfully engages with others, Asks challenging and probing questions in a manner that preserves healthy relationships</p></div>
      <div class="trait"><div class="trait-head"><span class="trait-num">05</span><span class="trait-name">Adaptable</span></div><p class="trait-text">Respectfully engages with others, Asks challenging and probing questions in a manner that preserves healthy relationships</p></div>
      <div class="trait"><div class="trait-head"><span class="trait-num">06</span><span class="trait-name">Curious</span></div><p class="trait-text">Respectfully engages with others, Asks challenging and probing questions in a manner that preserves healthy relationships</p></div>
    </div>
    <svg class="pointer" width="44" height="26" viewBox="0 0 44 26" aria-hidden="true"><polygon points="0,0 22,0 22,26" fill="var(--green-b)"/><polygon points="22,0 44,0 22,26" fill="var(--navy)"/></svg>
  </section>

  <section class="pillar" style="top:548px">
    <div class="pillar-art" role="img" aria-label="Illustration of two students talking together"></div>
    <div class="pillar-label">COLLABORATIVE</div>
    <div class="traits">
      <div class="trait"><div class="trait-head"><span class="trait-num">01</span><span class="trait-name">Emotional<br>Inteligence</span></div><p class="trait-text">Respectfully engages with others, Asks challenging and probing questions in a manner that preserves healthy relationships</p></div>
      <div class="trait"><div class="trait-head"><span class="trait-num">02</span><span class="trait-name">Civic Minded</span></div><p class="trait-text">Respectfully engages with others, Asks challenging and probing questions in a manner that preserves healthy relationships</p></div>
      <div class="trait"><div class="trait-head"><span class="trait-num">03</span><span class="trait-name">Compassionate<br>Leader</span></div><p class="trait-text">Respectfully engages with others, Asks challenging and probing questions in a manner that preserves healthy relationships</p></div>
      <div class="trait locked" style="background:var(--cell-dark)"><svg width="40" height="48" viewBox="0 0 40 48" aria-hidden="true" fill="none" stroke="#b8b9bd" stroke-width="2"><path d="M9 20 V13 a11 11 0 0 1 22 0 V20"/><path d="M13 20 V13 a7 7 0 0 1 14 0 V20"/><rect x="3" y="20" width="34" height="26" rx="3"/><circle cx="20" cy="31" r="3"/><path d="M20 34 v5"/></svg></div>
      <div class="trait locked" style="background:var(--cell-light)"><svg width="40" height="48" viewBox="0 0 40 48" aria-hidden="true" fill="none" stroke="#b8b9bd" stroke-width="2"><path d="M9 20 V13 a11 11 0 0 1 22 0 V20"/><path d="M13 20 V13 a7 7 0 0 1 14 0 V20"/><rect x="3" y="20" width="34" height="26" rx="3"/><circle cx="20" cy="31" r="3"/><path d="M20 34 v5"/></svg></div>
      <div class="trait locked" style="background:var(--cell-dark)"><svg width="40" height="48" viewBox="0 0 40 48" aria-hidden="true" fill="none" stroke="#b8b9bd" stroke-width="2"><path d="M9 20 V13 a11 11 0 0 1 22 0 V20"/><path d="M13 20 V13 a7 7 0 0 1 14 0 V20"/><rect x="3" y="20" width="34" height="26" rx="3"/><circle cx="20" cy="31" r="3"/><path d="M20 34 v5"/></svg></div>
    </div>
    <svg class="pointer" width="44" height="26" viewBox="0 0 44 26" aria-hidden="true"><polygon points="0,0 22,0 22,26" fill="var(--green-b)"/><polygon points="22,0 44,0 22,26" fill="var(--navy)"/></svg>
  </section>

  <section class="pillar" style="top:867px">
    <div class="pillar-art" role="img" aria-label="Illustration of a student holding a puzzle piece"></div>
    <div class="pillar-label">SELF-DIRECTED</div>
    <div class="traits">
      <div class="trait"><div class="trait-head"><span class="trait-num">01</span><span class="trait-name">Responsible</span></div><p class="trait-text">Respectfully engages with others, Asks challenging and probing questions in a manner that preserves healthy relationships</p></div>
      <div class="trait"><div class="trait-head"><span class="trait-num">02</span><span class="trait-name">Self-Starter</span></div><p class="trait-text">Respectfully engages with others, Asks challenging and probing questions in a manner that preserves healthy relationships</p></div>
      <div class="trait"><div class="trait-head"><span class="trait-num">03</span><span class="trait-name">Growth Mndset</span></div><p class="trait-text">Respectfully engages with others, Asks challenging and probing questions in a manner that preserves healthy relationships</p></div>
      <div class="trait"><div class="trait-head"><span class="trait-num">04</span><span class="trait-name">Problem Solving</span></div><p class="trait-text">Respectfully engages with others, Asks challenging and probing questions in a manner that preserves healthy relationships</p></div>
      <div class="trait"><div class="trait-head"><span class="trait-num">05</span><span class="trait-name">Resilient</span></div><p class="trait-text">Respectfully engages with others, Asks challenging and probing questions in a manner that preserves healthy relationships</p></div>
      <div class="trait locked" style="background:var(--cell-dark)"><svg width="40" height="48" viewBox="0 0 40 48" aria-hidden="true" fill="none" stroke="#b8b9bd" stroke-width="2"><path d="M9 20 V13 a11 11 0 0 1 22 0 V20"/><path d="M13 20 V13 a7 7 0 0 1 14 0 V20"/><rect x="3" y="20" width="34" height="26" rx="3"/><circle cx="20" cy="31" r="3"/><path d="M20 34 v5"/></svg></div>
    </div>
  </section>
</div>
</body>
</html>
```